Wordpress Design Project

Good day.

I was hoping to buy a professional looking Wordpress template and just fill in the blanks with my personal data and start blogging, but unfortunately my blog posts need to include images that are 756 pixels x 439.

A sample image can be found at.
http://files.brindlecache.net/7-Pics/layoutsample.gif

So, I need your help.

1 This is a daily newsletter / blog site only. Not a corporate site.
2 Subject - Stock Market
2 I have no color preferences. I will leave that up to you.
I would like something that looks like this
http://preview.loftmerath.com/clarity/
3 I would like to include Vortelli Ads on both the Home Page and within each post.
4 The home page should show a link and a short summary to each post.
5 The home page should include an email capture box. We use MailChimp)
6 The home page should include a Site Search Box and function.
7 The home page should include a External Links Box.

If I have forgotten anything, please let me know.
I welcome your suggestions.

I look forward to seeing your designs and picking a winner.

Thank you for reading my post.

Darren Oakhurst

Vortelli

```html
<!DOCTYPE html>
<html lang="en">
<head>
<meta charset="utf-8">
<title>Stock Market</title>
<link rel="stylesheet" href="https://fonts.googleapis.com/css2?family=Oswald:wght@400;500&family=Anton&family=Archivo+Black&family=Arimo:wght@400;700&display=swap">
<style>
:root{
  --accent:#1a9bd0;
  --header-bg:#eaf8fd;
  --nav-bg:#222222;
  --nav-rule:#444444;
  --footer-bg:#333333;
  --ink:#333333;
  --body-text:#222222;
  --muted:#8a8a8a;
  --placeholder:#c6c6c6;
  --placeholder-edge:#a9a9a9;
  --rule:#e2e2e2;
  --page:#ffffff;
}
*{margin:0;padding:0;box-sizing:border-box}
html,body{width:1117px;height:1200px;overflow:hidden;background:var(--page)}
body{position:relative;font-family:"Arimo",Arial,sans-serif;color:var(--body-text)}
.abs{position:absolute}

/* header */
.site-header{position:absolute;left:0;top:0;width:1117px;height:146px;background:var(--header-bg)}
.brand-title{position:absolute;left:131px;top:30px;font-family:"Oswald",sans-serif;font-weight:500;font-size:48px;line-height:1;color:var(--accent);letter-spacing:0.5px}
.brand-tagline{position:absolute;left:133px;top:93px;font-family:"Arimo",sans-serif;font-size:17px;letter-spacing:7.2px;color:#222}
.signup{position:absolute;left:661px;top:26px;width:327px;height:99px;border:1px solid #cfe6ef;border-radius:34px;background:#f5fcff}
.signup-title{position:absolute;left:15px;top:14px;font-size:21px;color:#222;white-space:nowrap}
.signup-title b{font-family:"Archivo Black",sans-serif;font-weight:400;font-size:27px;margin-left:6px;color:#1d1d1d}
.signup-field{position:absolute;top:57px;height:25px;border:1px solid #d8d8d8;background:#fff;border-radius:3px;font-size:10px;color:#666;padding:6px 6px}
.signup-btn{position:absolute;left:269px;top:58px;width:44px;height:24px;background:var(--accent);color:#fff;border-radius:4px;font-size:10.5px;text-align:center;line-height:24px}

/* nav */
.main-nav{position:absolute;left:0;top:146px;width:1117px;height:45px;background:var(--nav-bg)}
.main-nav a{position:absolute;top:0;height:45px;line-height:45px;color:#fff;font-size:14px;text-decoration:none;text-align:center}
.nav-sep{position:absolute;top:3px;width:1px;height:42px;background:var(--nav-rule)}
.search-input{position:absolute;left:803px;top:12px;width:144px;height:24px;background:#fff;border:1px solid #999;font-size:12px;color:#777;padding:5px 6px}
.search-go{position:absolute;left:948px;top:12px;width:28px;height:24px;background:#3a3a3a;color:#fff;font-size:15px;line-height:24px;text-align:center}

/* posts */
.post-title{position:absolute;left:128px;font-family:"Archivo Black",sans-serif;font-size:30px;color:var(--ink);line-height:1;white-space:nowrap}
.post-meta{position:absolute;left:128px;width:402px;height:18px;background:linear-gradient(90deg,#e5f5fc 70%,rgba(229,245,252,0));font-size:10.5px;color:var(--accent);padding:3px 8px}
.post-excerpt{position:absolute;left:129px;width:650px;font-size:12.3px;line-height:14.5px;color:#222}
.read-more{color:#111;font-size:13.5px;text-decoration:underline;text-underline-offset:2px}
.placeholder{position:absolute;left:128px;width:651px;background:var(--placeholder);border:1px solid var(--placeholder-edge);display:flex;align-items:center;justify-content:center;font-family:"Archivo Black",sans-serif;color:#e2e2e2;-webkit-text-stroke:1px #a8a8a8}
.view-all{position:absolute;left:690px;top:1068px;font-size:13px;color:var(--accent);text-decoration:underline}

/* sidebar */
.side-label{position:absolute;left:827px;top:224px;font-size:16px;color:#333}
.social-dot{position:absolute;top:256px;width:28px;height:28px;border-radius:50%;background:var(--accent)}
.side-rule{position:absolute;left:827px;width:162px;height:1px;background:var(--rule)}
.side-heading{position:absolute;left:827px;font-family:"Anton",sans-serif;font-size:24px;color:var(--accent);line-height:1}
.side-text{position:absolute;left:827px;width:164px;top:378px;font-size:12.1px;line-height:14.5px;color:#222}
.side-list{position:absolute;left:827px;list-style:none}
.side-list li{height:25.8px;font-size:13px;color:#333;padding-left:16px;position:relative;line-height:16px}
.side-list li::before{content:"";position:absolute;left:1px;top:4px;border-left:5px solid #222;border-top:4px solid transparent;border-bottom:4px solid transparent}

/* footer */
.site-footer{position:absolute;left:0;top:1128px;width:1117px;height:72px;background:var(--footer-bg)}
.footer-links{position:absolute;left:129px;top:15px;font-size:13px;color:#eee;white-space:nowrap}
.footer-links span{display:inline-block}
.footer-copy{position:absolute;left:129px;top:43px;font-size:10px;color:#8c8c8c}
</style>
</head>
<body>

<header class="site-header">
  <div class="brand-title">STOCK MARKET</div>
  <div class="brand-tagline">YOUR TITLE HERE</div>
  <div class="signup">
    <div class="signup-title">SIGN UP<b>Newsletter</b></div>
    <div class="signup-field" style="left:15px;width:113px">Enter your first name</div>
    <div class="signup-field" style="left:131px;width:134px">Enter your email address</div>
    <div class="signup-btn">Sign up</div>
  </div>
</header>

<nav class="main-nav">
  <a href="#" style="left:132px;width:66px">HOME</a>
  <span class="nav-sep" style="left:198px"></span>
  <a href="#" style="left:199px;width:100px">ABOUT ME</a>
  <span class="nav-sep" style="left:299px"></span>
  <a href="#" style="left:300px;width:93px">MARKET</a>
  <span class="nav-sep" style="left:393px"></span>
  <a href="#" style="left:394px;width:98px">STOCKS</a>
  <span class="nav-sep" style="left:492px"></span>
  <a href="#" style="left:493px;width:105px">PROPERTY</a>
  <span class="nav-sep" style="left:598px"></span>
  <a href="#" style="left:599px;width:116px">CONTACT US</a>
  <div class="search-input">Search here</div>
  <div class="search-go">GO</div>
</nav>

<main>
  <h2 class="post-title" style="top:222px">Lorem ipsum dolor sit amet</h2>
  <div class="post-meta" style="top:264px">Posted on 17 March, 2013 | Leave a comment</div>
  <p class="post-excerpt" style="top:295px">Pellentesque facilisis euismod mattis. Duis scelerisque enim eget velit viverra porta. Nunc et leo at nibh ultrices placerat eu eu erat. Nunc viverra, neque vitae varius tristique, massa nunc facilisis est, ut gravida eros lorem quis velit. Phasellus accumsan semper leo. Quisque eget dolor sem. Morbi sit amet commodo ipsum, et tincidunt nisl. Fusce laoreet tellus vitae augue venenatis, eu vulputate neque blandit. Morbi posuere felis quis tellus hendrerit luctus in eget arcu. Aliquam porta purus ipsum. Aliquam aliquet euismod feugiat. Nullam suscipit ac lorem nec viverra. <a class="read-more" href="#">Read more</a></p>

  <div class="placeholder" role="img" aria-label="Post feature image area" style="top:390px;height:379px;font-size:40px">IMAGE COMES HERE</div>
  <div class="placeholder" role="img" aria-label="Advertisement banner area" style="top:779px;height:86px;font-size:40px">AD HERE</div>

  <h2 class="post-title" style="top:876px">Lorem ipsum dolor sit amet</h2>
  <div class="post-meta" style="top:918px">Posted on 17 March, 2013 | Leave a comment</div>
  <p class="post-excerpt" style="top:973px">Aliquam convallis lorem eget metus scelerisque euismod ultrices eu tellus. Morbi at lobortis ante. Sed rhoncus libero id magna accumsan, quis viverra eros dapibus. Cum sociis natoque penatibus et magnis dis parturient montes, nascetur ridiculus mus. Maecenas consequat fringilla tellus. Proin posuere tempus tincidunt. Integer vitae tempus erat. Nam pretium arcu quis tortor volutpat, a fermentum quam feugiat. Nullam laoreet libero accumsan metus eleifend, vitae sollicitudin eros facilisis. Vestibulum bibendum mauris ac arcu lacinia, vel euismod felis aliquet. Donec commodo turpis non iaculis placerat. <a class="read-more" href="#">Read more</a></p>
  <a class="view-all" href="#">View all post</a>
</main>

<aside>
  <div class="side-label">Connect with me:</div>
  <span class="social-dot" style="left:827px" aria-label="Social profile"></span>
  <span class="social-dot" style="left:859px" aria-label="Social profile"></span>
  <span class="social-dot" style="left:891px" aria-label="Share"></span>
  <div class="side-rule" style="top:311px"></div>

  <h3 class="side-heading" style="top:338px">About me</h3>
  <p class="side-text">Sed pulvinar pellentesque massa sed vestibulum. In consequat condimentum mi, sit amet ornare justo interdum sed. Sed fringilla lorem at justo rutrum, sed consectetur neque congue. Donec volutpat accumsan magna, ac gravida est pulvinar vitae. Phasellus volutpat dictum arcu, non sagittis velit rutrum feugiat. Mauris a nisi magna. Maecenas sem urna, volutpat non nibh in, venenatis ullamcorper neque.</p>
  <div class="side-rule" style="top:620px"></div>

  <h3 class="side-heading" style="top:640px">Blogroll</h3>
  <ul class="side-list" style="top:682px"><li>Curabitur elementum</li></ul>
  <div class="side-rule" style="top:722px"></div>

  <h3 class="side-heading" style="top:749px">Categories</h3>
  <ul class="side-list" style="top:790px">
    <li>Lorem ipsum dolor</li>
    <li>Curabitur elementum</li>
    <li>Lorem ipsum dolor</li>
    <li>Curabitur elementum</li>
    <li>Lorem ipsum dolo</li>
    <li>Lorem ipsum dolor</li>
    <li>Curabitur elementum</li>
    <li>Curabitur elementum</li>
  </ul>
</aside>

<footer class="site-footer">
  <div class="footer-links">
    <span style="width:47px">home</span><span style="width:18px">|</span><span style="width:75px">about me</span><span style="width:30px">|</span><span style="width:60px">Market</span><span style="width:20px">|</span><span style="width:64px">Stocks</span><span style="width:30px">|</span><span style="width:62px">Property</span><span style="width:12px">|</span><span>Contact us</span>
  </div>
  <div class="footer-copy">Copyright 2013 harborlinepress.com All Rights Reserved.</div>
</footer>

</body>
</html>
```